Zielgruppe
Massagen und Therapien an Patienten mit Schmerzen an Muskeln und am gesamten Bewegungsapparat. Nachbehandlung nach Operationen und Verletzungen sowie Sportverletzungen therapieren.
Zielgruppe: alle Personen (m/w) jeden alters egal ob sportlich oder 'faul'.
Aufgabenstellung
Das Design soll Ruhe, Harmonie, Vertrautheit und Geborgenheit vermitteln. Es muß mit dem Firmenlogo harmonisieren (Farbe und Gestaltung).
Das Logo und der Text findet sich im Anhang.
Es können Bilder eigenständig hinzugefügt werden.
Unbedingt DIN-Format verwenden (welches bleibt dem Designer überlassen)

```html
<!DOCTYPE html>
<html lang="de">
<head>
<meta charset="utf-8">
<title>med. Massagepraxis Lindqvorst – Faltblatt</title>
<link rel="stylesheet" href="https://fonts.googleapis.com/css2?family=Arimo:wght@400;700&family=Questrial&family=Tinos&display=swap">
<style>
  :root {
    --blue: #4a7fc1;
    --blue-light: #a9c4e6;
    --green: #8dbb2e;
    --green-pale: #f0f5e4;
    --text: #4b4b4b;
    --stage: #ecebe8;
    --paper: #ffffff;
    --fold: rgba(0,0,0,0.07);
  }
  * { box-sizing: border-box; margin: 0; padding: 0; }
  html, body { width: 1200px; height: 667px; overflow: hidden; }
  body {
    background: var(--stage);
    font-family: "Questrial", "Helvetica Neue", sans-serif;
    color: var(--text);
    position: relative;
  }
  .spread {
    position: absolute;
    top: 128px;
    width: 580px;
    height: 410px;
    background: var(--paper);
    box-shadow: 0 2px 10px rgba(0,0,0,0.12);
    overflow: hidden;
  }
  .spread--outside { left: 13px; }
  .spread--inside { left: 607px; }
  .spread__bands { position: absolute; inset: 0; width: 580px; height: 410px; }
  .panel {
    position: absolute;
    top: 0;
    width: 193.33px;
    height: 410px;
  }
  .panel--1 { left: 0; }
  .panel--2 { left: 193.33px; border-left: 1px solid var(--fold); }
  .panel--3 { left: 386.66px; border-left: 1px solid var(--fold); }
  .panel__title {
    position: absolute;
    left: 12px; top: 24px;
    font-family: "Arimo", Arial, sans-serif;
    font-weight: 700;
    font-size: 9px;
    color: #fff;
  }
  .photo {
    position: absolute;
    left: 0; right: 0;
  }
  .body-text {
    position: absolute;
    left: 14px; right: 12px;
    font-size: 5.6px;
    line-height: 1.45;
  }
  .body-text p { margin-bottom: 5px; }
  .body-text .hl { color: var(--blue); font-weight: 700; }
  .list-head { font-family: "Arimo", Arial, sans-serif; font-weight: 700; font-size: 5.8px; margin-top: 4px; }
  .bullets { list-style: none; }
  .bullets li { padding-left: 6px; position: relative; }
  .bullets li::before {
    content: ""; position: absolute; left: 0; top: 2.6px;
    width: 3px; height: 3px; border-radius: 50%; background: var(--blue);
  }
  .arrow { color: var(--green); }
  .foot-note {
    position: absolute;
    left: 14px; right: 12px;
    font-size: 5.8px;
    line-height: 1.4;
    color: var(--green);
  }
  .wordmark {
    position: absolute;
    left: 0; right: 0;
    text-align: center;
    color: var(--blue);
    font-family: "Questrial", sans-serif;
  }
  .wordmark__dot {
    display: block;
    margin: 0 auto 6px;
    border-radius: 50%;
    background: var(--green);
  }
  .placeholder-note {
    position: absolute; left: 0; right: 0; top: 80px;
    text-align: center;
    font-family: "Tinos", "Times New Roman", serif;
    font-size: 8px; color: #333;
  }
  .address {
    position: absolute; left: 0; right: 0; top: 262px;
    text-align: center; font-size: 5.6px; line-height: 1.5; color: #333;
  }
  .cover-grid {
    position: absolute; left: 34px; top: 120px;
    width: 126px; height: 132px;
    display: grid; grid-template-columns: repeat(3, 1fr); grid-template-rows: repeat(3, 1fr); gap: 3px;
  }
  .cover-grid div { border-radius: 1px; }
  .tagline {
    position: absolute; left: 0; right: 0; top: 268px;
    text-align: center; color: var(--green); font-size: 8.5px;
  }
  .services {
    position: absolute; left: 8px; right: 8px; top: 330px;
    text-align: center; color: var(--blue); font-size: 6.4px; line-height: 1.45;
  }
</style>
</head>
<body>

<section class="spread spread--outside">
  <svg class="spread__bands" viewBox="0 0 580 410" aria-hidden="true">
    <path d="M0 0 H386 V14 C300 30 190 50 0 60 Z" fill="var(--blue)"/>
    <path d="M0 60 C190 50 300 30 386 14 V20 C300 36 190 56 0 66 Z" fill="var(--blue-light)"/>
    <path d="M0 351 C200 341 400 321 580 298 V410 H0 Z" fill="var(--green-pale)"/>
    <path d="M0 345 C200 335 400 315 580 292 V298 C400 321 200 341 0 351 Z" fill="var(--green)"/>
  </svg>

  <div class="panel panel--1">
    <h2 class="panel__title">Akupunk-Massage nach Dorneck</h2>
    <div class="photo" style="top:66px;height:140px;background:linear-gradient(160deg,#e9e4de,#d9c2ad 55%,#f4f1ee);" role="img" aria-label="Foto: Behandlung einer Patientin im Gesicht mit einem Massagestäbchen"></div>
    <div class="body-text" style="top:216px;">
      <p>Durch diese Behandlungsmethode können viele Beschwerde- und Krankheitsbilder beeinflusst werden, die durch funktionelle Störungen im Körper verursacht worden sind.</p>
      <div class="list-head">Indikationen:</div>
      <ul class="bullets">
        <li>Wirbelsäulenbeschwerden</li>
        <li>Migräne</li>
        <li>Erkrankungen der Gelenke</li>
        <li>Neuralgien</li>
        <li>Durchblutungsstörungen</li>
        <li>u.v.m.</li>
      </ul>
    </div>
  </div>

  <div class="panel panel--2">
    <p class="placeholder-note">Team/Praxisfoto hier?</p>
    <div class="wordmark" style="top:210px;font-size:9px;">
      <span class="wordmark__dot" style="width:12px;height:12px;"></span>
      med. Massagepraxis Lindqvorst
    </div>
    <div class="address">
      Jonas Lindqvorst<br>
      Amselgasse 7 Haus 4<br>
      3012 Kirchbergen<br>
      Tel +43 660 000 12 34
    </div>
    <p class="foot-note" style="top:362px;text-align:center;">Hausbesuche auf Anfrage</p>
  </div>

  <div class="panel panel--3">
    <div class="wordmark" style="top:36px;font-size:13px;line-height:1.2;">
      <span class="wordmark__dot" style="width:20px;height:20px;"></span>
      med. Massagepraxis<br>Lindqvorst
    </div>
    <div class="cover-grid" role="img" aria-label="Fotoraster: neun Nahaufnahmen von Massagegriffen an Schulter, Rücken, Knie und Händen">
      <div style="background:#e3cdbb"></div>
      <div style="background:#d8c79a"></div>
      <div style="background:#e7c9b3"></div>
      <div style="background:#d9dcc0"></div>
      <div style="background:#e2b8a7"></div>
      <div style="background:#d7cdd9"></div>
      <div style="background:#dcc6d6"></div>
      <div style="background:#d3b49c"></div>
      <div style="background:#e4d6c9"></div>
    </div>
    <p class="tagline">Schmerzfrei und vital leben</p>
    <p class="services">EMS Training · Massage · Lymphdrainage ·<br>Akupunk-Massage nach Dorneck</p>
  </div>
</section>

<section class="spread spread--inside">
  <svg class="spread__bands" viewBox="0 0 580 410" aria-hidden="true">
    <path d="M0 0 H580 V30 C420 20 250 28 0 44 Z" fill="var(--blue)"/>
    <path d="M0 44 C250 28 420 20 580 30 V35 C420 26 250 34 0 50 Z" fill="var(--blue-light)"/>
    <path d="M0 360 C200 342 400 326 580 318 V410 H0 Z" fill="var(--green-pale)"/>
    <path d="M0 353 C200 334 400 318 580 310 V316 C400 324 200 340 0 360 Z" fill="var(--green)"/>
  </svg>

  <div class="panel panel--1">
    <h2 class="panel__title" style="top:16px;">EMS-Ganzkörpertraining</h2>
    <div class="photo" style="top:42px;height:110px;background:linear-gradient(150deg,#c98c6c,#e0a888 60%,#b77358);" role="img" aria-label="Foto: Rücken mit aufgeklebten EMS-Elektroden"></div>
    <div class="body-text" style="top:160px;">
      <p><span class="hl">EMS (Elektro-Muskel-Stimulation)</span> ist eine neue Dimension des Ganzkörpertrainings.</p>
      <p>Schneller und intensiver als mit herkömmlichen Methoden, in weniger als 20 Minuten / Trainingseinheit und 1x pro Woche.</p>
      <p>Dadurch kann effektiv und effizient trainiert werden, in allen Alters- und Leistungsstufen.</p>
      <ul class="bullets">
        <li>Gesundheit bedeutet Lebensqualität</li>
        <li>für einen leistungsfähigen Körper</li>
        <li>Schlank &amp; Straff</li>
        <li>Fit im Sport</li>
      </ul>
    </div>
  </div>

  <div class="panel panel--2">
    <h2 class="panel__title" style="top:16px;">Massage</h2>
    <div class="photo" style="top:42px;height:110px;background:linear-gradient(150deg,#d8d6d2,#c9a996 50%,#6fa3c9);" role="img" aria-label="Foto: Therapeut massiert die Schulter einer Patientin"></div>
    <div class="body-text" style="top:160px;">
      <p>Die <span class="hl">klassische Massage</span> dient vor allem zur Behandlung verspannter Muskulatur oder zur Vorbeugung von Verspannungen.</p>
      <div class="list-head">Indikationen:</div>
      <ul class="bullets">
        <li>Bewegungseinschränkung durch Verspannungen am Rücken, Brust, Schulter, etc.</li>
        <li>Spannungskopfschmerzen</li>
        <li>Muskelschmerzen</li>
        <li>zur schnellen Regeneration nach dem Sport oder nach Verletzungen</li>
        <li>fördert die seelische und körperliche Ausgeglichenheit</li>
        <li>stabilisiert das Immunsystem</li>
        <li>verbessert den Lymphfluss</li>
        <li>wirkt sich positiv auf die Durchblutung der Haut und des Bindegewebes aus</li>
      </ul>
    </div>
    <p class="foot-note" style="top:372px;">Die Massagetherapie wird nach ärztlicher Verordnung durchgeführt.</p>
  </div>

  <div class="panel panel--3">
    <h2 class="panel__title" style="top:16px;">Lymphdrainage</h2>
    <div class="photo" style="top:42px;height:110px;background:linear-gradient(150deg,#e6ddd4,#d6a98c 55%,#efe7df);" role="img" aria-label="Foto: Lymphdrainage am Knie"></div>
    <div class="body-text" style="top:166px;">
      <p>Die sanften, schmerzfreien und langsam ausgeführten Griffe wirken:</p>
      <ul class="bullets">
        <li>Entwässernd <span class="arrow">▸</span> entstauend</li>
        <li>Entgiftend <span class="arrow">▸</span> entschlackend</li>
        <li>Beruhigend <span class="arrow">▸</span> entspannend</li>
        <li>stärken das Immunsystem</li>
        <li>bei Rheumatischen Schwellungen</li>
      </ul>
      <div class="list-head">Indikationen:</div>
      <ul class="bullets">
        <li>nach Operationen</li>
        <li>nach Tumorbehandlungen</li>
        <li>nach Verletzungen</li>
        <li>nach Lymphknotenentfernungen</li>
        <li>nach Hämatomen (Bluterguß)</li>
        <li>hoher Muskeltonus</li>
      </ul>
    </div>
    <p class="foot-note" style="top:366px;">Über das Lymphsystem werden die meisten Abfallprodukte des Körpers abtransportiert.</p>
  </div>
</section>

</body>
</html>
```